Business Card Design

Electrical Contracting buisness
need a buisness card relating to that buisness

Reason: Just need to discuss with partner

Industry/Entity Type

Business

Contact Information for Business Card

Colin Harbage Electrical
0417 562 983
colinharbage7@mailvessel.com
REC 48761

```html
<!DOCTYPE html>
<html lang="en">
<head>
<meta charset="utf-8">
<title>Colin Harbage Electrical – Business Card</title>
<link href="https://fonts.googleapis.com/css2?family=Noto+Serif:wght@400;700&display=swap" rel="stylesheet">
<style>
  :root {
    --page-bg: #1c1c1c;
    --card-dark: #2b2b2d;
    --card-mid: #4a4a4c;
    --text-light: #f2f2f2;
    --text-muted: #d6d6d6;
    --band-white: #f4f4f4;
    --band-green: #7cc62e;
    --band-green-light: #a6dc55;
    --phone-ink: #111111;
  }
  html, body {
    margin: 0;
    width: 1200px;
    height: 900px;
    overflow: hidden;
    background: var(--page-bg);
    font-family: "Noto Serif", Georgia, serif;
  }
  .card {
    position: absolute;
    left: 100px;
    top: 150px;
    width: 1000px;
    height: 600px;
    overflow: hidden;
    background: linear-gradient(160deg, var(--card-mid) 0%, var(--card-dark) 70%);
    box-shadow: 0 20px 50px rgba(0,0,0,0.6);
  }
  .card-art {
    position: absolute;
    inset: 0;
  }
  .business-name {
    position: absolute;
    left: 520px;
    top: 70px;
    width: 420px;
    margin: 0;
    text-align: center;
    color: var(--text-light);
    font-weight: 700;
    font-size: 40px;
    line-height: 1.05;
    letter-spacing: 0.5px;
  }
  .contact-person {
    position: absolute;
    left: 560px;
    top: 200px;
    width: 340px;
    text-align: center;
    color: var(--text-muted);
  }
  .contact-person .person-name {
    font-size: 22px;
    letter-spacing: 1px;
    line-height: 1.1;
  }
  .contact-person .person-role {
    font-size: 12px;
    letter-spacing: 1.5px;
  }
  .email {
    position: absolute;
    right: 70px;
    top: 318px;
    color: var(--text-muted);
    font-size: 18px;
  }
  .phone {
    position: absolute;
    right: 70px;
    top: 372px;
    height: 58px;
    line-height: 58px;
    color: var(--phone-ink);
    font-size: 40px;
    letter-spacing: 1px;
  }
</style>
</head>
<body>
  <div class="card">
    <svg class="card-art" width="1000" height="600" viewBox="0 0 1000 600">
      <defs>
        <linearGradient id="wireTones" x1="0" y1="0" x2="1" y2="1">
          <stop offset="0" stop-color="#2d5f9e"/>
          <stop offset="0.35" stop-color="#b8764a"/>
          <stop offset="0.6" stop-color="#5a5a5c"/>
          <stop offset="0.85" stop-color="#a9a23a"/>
          <stop offset="1" stop-color="#3a3a3c"/>
        </linearGradient>
        <linearGradient id="greenBand" x1="0" y1="0" x2="0" y2="1">
          <stop offset="0" stop-color="var(--band-green-light)"/>
          <stop offset="1" stop-color="var(--band-green)"/>
        </linearGradient>
      </defs>
      <g class="contact-bands">
        <rect x="480" y="355" width="520" height="120" fill="var(--band-white)"/>
        <rect x="480" y="372" width="520" height="58" fill="url(#greenBand)"/>
      </g>
      <path class="wire-photo" role="img" aria-label="Close-up photograph of stripped electrical cables with copper strands and blue, brown, grey and yellow-green insulation"
            d="M0 0 H440 C580 110 620 380 520 600 H0 Z" fill="url(#wireTones)"/>
    </svg>

    <h1 class="business-name">Colin Harbage<br>Electrical</h1>
    <div class="contact-person">
      <div class="person-name">PETER LANDRY</div>
      <div class="person-role">GENERAL MANAGER</div>
    </div>
    <div class="email">colinharbage7@mailvessel.com</div>
    <div class="phone">0417 562 983</div>
  </div>
</body>
</html>
```